Business Card

I need a business card that really pops for a potential customer or person who refers a personal injury lead. I want to highlight our office locations, but only address that needs to be on the card is my office's main address. I want a sleek, modern and minimalist design.

```html
<!DOCTYPE html>
<html lang="en">
<head>
<meta charset="utf-8">
<title>Northgate Injury Lawyers — Business Card</title>
<link href="https://fonts.googleapis.com/css2?family=Jost:wght@300;400&display=swap" rel="stylesheet">
<style>
  :root {
    --backdrop: #1c1d1e;
    --card: #3b3c3d;
    --ink: #dcdcdc;
    --ink-soft: #c4c4c4;
  }
  html, body {
    margin: 0;
    padding: 0;
    width: 1200px;
    height: 900px;
    overflow: hidden;
    background: var(--backdrop);
  }
  .canvas {
    width: 1200px;
    height: 900px;
    display: flex;
    align-items: center;
    justify-content: center;
  }
  .card {
    position: relative;
    width: 1000px;
    height: 572px;
    background: var(--card);
    color: var(--ink);
    font-family: "Jost", "Futura", sans-serif;
    font-weight: 300;
    box-sizing: border-box;
  }
  .holder {
    position: absolute;
    top: 62px;
    left: 72px;
  }
  .holder-name {
    margin: 0;
    font-size: 34px;
    font-weight: 400;
    letter-spacing: 0.04em;
    text-transform: uppercase;
  }
  .holder-title {
    margin: 2px 0 0;
    font-size: 21px;
    letter-spacing: 0.05em;
    text-transform: uppercase;
    color: var(--ink-soft);
  }
  .locations {
    position: absolute;
    top: 190px;
    right: 66px;
    margin: 0;
    padding: 0;
    list-style: none;
    font-size: 19px;
    line-height: 1.3;
    text-transform: uppercase;
    color: var(--ink-soft);
  }
  .locations li {
    display: flex;
    align-items: center;
    justify-content: flex-end;
    gap: 3px;
  }
  .pin {
    width: 12px;
    height: 16px;
    fill: var(--ink-soft);
  }
  .firm-name {
    position: absolute;
    top: 262px;
    left: 0;
    width: 100%;
    display: flex;
    align-items: center;
    justify-content: center;
    gap: 14px;
    margin: 0;
    font-size: 38px;
    font-weight: 300;
    line-height: 1;
    color: var(--ink);
  }
  .firm-dot {
    width: 12px;
    height: 12px;
    border-radius: 50%;
    background: var(--ink);
  }
  .contact {
    position: absolute;
    left: 72px;
    bottom: 78px;
    font-size: 21px;
    line-height: 1.45;
    color: var(--ink-soft);
  }
  .contact p, .address p { margin: 0; }
  .address {
    position: absolute;
    right: 66px;
    bottom: 40px;
    text-align: right;
    font-size: 21px;
    font-style: normal;
    line-height: 1.3;
    color: var(--ink-soft);
  }
</style>
</head>
<body>
<main class="canvas">
  <article class="card">
    <header class="holder">
      <h1 class="holder-name">Daniel Carver</h1>
      <p class="holder-title">Managing Director</p>
    </header>

    <ul class="locations">
      <li>Chicago
        <svg class="pin" viewBox="0 0 12 16" aria-hidden="true"><path d="M6 0a6 6 0 0 0-6 6c0 4.5 6 10 6 10s6-5.5 6-10a6 6 0 0 0-6-6zm0 8.5A2.5 2.5 0 1 1 6 3.5a2.5 2.5 0 0 1 0 5z"/></svg>
      </li>
      <li>Indiana
        <svg class="pin" viewBox="0 0 12 16" aria-hidden="true"><path d="M6 0a6 6 0 0 0-6 6c0 4.5 6 10 6 10s6-5.5 6-10a6 6 0 0 0-6-6zm0 8.5A2.5 2.5 0 1 1 6 3.5a2.5 2.5 0 0 1 0 5z"/></svg>
      </li>
      <li>Joliet
        <svg class="pin" viewBox="0 0 12 16" aria-hidden="true"><path d="M6 0a6 6 0 0 0-6 6c0 4.5 6 10 6 10s6-5.5 6-10a6 6 0 0 0-6-6zm0 8.5A2.5 2.5 0 1 1 6 3.5a2.5 2.5 0 0 1 0 5z"/></svg>
      </li>
    </ul>

    <p class="firm-name"><span class="firm-dot" aria-hidden="true"></span>Northgate Injury Lawyers</p>

    <div class="contact">
      <p>(312) 555-0148</p>
      <p>dcarver@northgateinjurylawyers.com</p>
      <p>www.northgateinjurylawyers.com</p>
    </div>

    <address class="address">
      <p>240 West Lake Street</p>
      <p>Suite 1800</p>
      <p>Chicago, IL 60601</p>
    </address>
  </article>
</main>
</body>
</html>
```